Vantix 220 for iPad

We are looking to design a page for the mobile app. The app is intended for financial professionals and is based on a successful desktop application. The existing design will serve as a very rough guideline, but we are open to hearing ideas.
Uploaded file #1 contains a screenshot of the existing design. The workflow is as follows:
The user picks a portfolio from the Dropdown below portfolio.
The user picks a Loss Threshold, which will dictate what gets onto the bubble chart below.
Once the bubble on the chart is clicked, a text box pops up with the description of the particular crisis that the bubble represents.
Once the bubble is clicked, the right hand side bar charts are populated with moves relevant to this scenario.
The left hand pane contains two text boxes. The lower one is particularly important, because the user is able to remove scenarios or add scenarios (screen #2). Removing scenarios is simple.
Adding scenarios brings up a wizard (screen #3). It also needs to be designed consistently with the front page of the app. The wizard has different clickable categories going down the column on the left and in a row on the top. The user can pick some or all of these categories.

Notes: The app should be designed for landscape mode only. The key to keep in mind is how the user will select bubbles on the chart. Right now, it is quite easy, but with the touchscreen it may be more complicated, so please keep that in mind when designing the chart (it should still be some version of the similar chart).
*As a first pass, please submit your idea of the concept (layout/colors/buttons) without the detailed design. We will choose 1-3 concepts and then the detailed work will take place with a much higher chance of a payout.
Updates

Thank you for the first two sketches. The second one by bertrand appears to be a bit more mobile app oriented, though we are still considering both and waiting for other submissions. One request, could you rework the sketches to include a bit more of dark blue as a background?  \

Bertrand, I think that the bubbles are too small and they are missing some volume effects. Could you make them a bit more prominent (and pick some form of dark blue background) and change the color to see if they will stand out better?
 

Industry/Entity Type

Financial

Requirements
Must have
• The general outline for the bubble chart must be retained. But the actual execution may differ significantly. We are open to seeing different ideas.
The winning design will also get a contract to design the rest of the application (2 more screens), which will be worth the same as the original design.

```html
<!DOCTYPE html>
<html lang="en">
<head>
<meta charset="utf-8">
<title>Vantix 220</title>
<link href="https://fonts.googleapis.com/css2?family=Arimo:wght@400;700&family=Varela+Round&display=swap" rel="stylesheet">
<style>
:root{
  --page:#ffffff;
  --screen:#252525;
  --nav:#2e2e2e;
  --nav-line:#444;
  --chart-bg:#1b1b1b;
  --grid:#3b3b3b;
  --yellow:#f5c000;
  --blue:#1a93dc;
  --green:#7cc42a;
  --red:#e0202a;
  --text:#ffffff;
  --muted:#bbbbbb;
  --panel:#1e1e1e;
  --panel-border:#777;
  --row-alt:#e4e4e4;
}
*{box-sizing:border-box;margin:0;padding:0}
html,body{width:1200px;height:1000px;overflow:hidden;background:var(--page)}
body{font-family:"Arimo",Arial,sans-serif;color:var(--text)}
.app{position:absolute;left:0;top:51px;width:880px;height:658px;background:var(--screen);transform:scale(1.3636);transform-origin:0 0;overflow:hidden}
.abs{position:absolute}

/* navigation */
.nav{position:absolute;left:0;top:0;width:880px;height:35px;background:linear-gradient(#3a3a3a,#262626);border-bottom:1px solid #111}
.nav-item{position:absolute;top:0;height:35px;line-height:35px;font-size:12px;color:#eee;transform:translateX(-50%);white-space:nowrap}
.nav-sep{position:absolute;top:0;width:1px;height:35px;background:var(--nav-line)}
.swatch{position:absolute;top:10px;width:16px;height:16px;border-radius:50%}
.hint-mark{color:#9ab4ff;font-weight:700}

/* header row */
.portfolio-select{left:23px;top:46px;width:524px;height:28px;background:var(--yellow);border-radius:3px;color:#111;font-weight:700;font-size:15px;line-height:28px;padding-left:11px}
.portfolio-select .caret{position:absolute;right:10px;top:12px;border:4px solid transparent;border-top:5px solid #111}
.doc-button{left:552px;top:46px;width:38px;height:28px;background:#fff;border-radius:3px}
.app-title{left:600px;top:46px;width:268px;height:28px;background:var(--green);border-radius:3px;font-family:"Varela Round",Arial,sans-serif;font-size:20px;line-height:28px;text-align:center;color:#fff}

/* controls */
.control-label{position:absolute;left:0;width:148px;text-align:center;font-size:11px;color:#eee}
.control{position:absolute;left:28px;width:92px;height:28px;background:var(--blue);border-radius:3px;text-align:center;font-size:12px;font-weight:700;line-height:28px;color:#fff}
.control.select{padding-right:12px}
.control.select::after{content:"";position:absolute;right:8px;top:12px;border:4px solid transparent;border-top:5px solid #fff}
.check{position:absolute;left:68px;top:446px;width:13px;height:13px;background:#fff;border:1px solid #8ab}
.search{position:absolute;left:8px;top:482px;width:130px;height:28px;background:#e6e6e6;border-radius:4px}

/* chart */
.chart{left:167px;top:84px;width:425px;height:440px;background:var(--chart-bg);border:1px solid #666}
.axis-tab{position:absolute;background:#ccc;color:#111;font-size:8px;font-weight:700;border-radius:2px;padding:2px 5px}
.tick-y{position:absolute;left:140px;width:20px;text-align:right;font-size:8px;color:#ccc}
.tick-x{position:absolute;top:528px;width:20px;text-align:center;font-size:8px;color:#ccc;transform:translateX(-50%)}
.tooltip{left:267px;top:318px;width:146px;height:58px;background:#fff;border-radius:3px;color:#111;text-align:center}
.tooltip-title{background:var(--yellow);font-weight:700;font-size:10px;height:16px;line-height:16px;border-radius:3px 3px 0 0}
.tooltip-body{font-size:9.5px;line-height:12px;padding-top:2px}
.tooltip::after{content:"";position:absolute;left:11px;bottom:-6px;border:6px solid transparent;border-bottom:0;border-top-color:#fff}

/* contribution panels */
.contrib{left:600px;width:268px;height:216px;background:var(--panel);border:2px solid var(--panel-border)}
.contrib-head{height:20px;line-height:20px;text-align:center;font-size:10px;font-weight:700;background:linear-gradient(#4a4a4a,#2a2a2a)}
.contrib-plot{position:absolute;left:110px;top:26px;width:152px;height:166px;background:#141414}
.row{position:absolute;left:0;height:14px;font-size:8px;line-height:14px}
.row .name{position:absolute;left:0;width:67px;text-align:right;color:var(--yellow);font-weight:700}
.row .date{position:absolute;left:72px;width:40px;color:#ddd}
.row .bar{position:absolute;top:6px;height:3px}
.row .pill{position:absolute;top:1px;height:12px;padding:0 3px;border-radius:3px;font-size:8px;line-height:12px;color:#fff}
.pos .bar,.pos .pill{background:var(--green)}
.neg .bar,.neg .pill{background:var(--red)}
.scale{position:absolute;font-size:7px;color:#ccc;transform:translateX(-50%)}

/* tables */
.table-panel{top:536px;height:114px;background:#fff;color:#111;border-radius:6px 6px 0 0;overflow:hidden}
.table-title{height:18px;line-height:18px;text-align:center;font-size:10px;font-weight:700;color:#fff;background:linear-gradient(#555,#333)}
table{width:100%;border-collapse:collapse;font-size:11px}
th{background:linear-gradient(#666,#444);color:#fff;font-weight:400;text-align:left;height:18px;padding-left:14px;border-right:1px solid #888}
td{height:16.5px;padding-left:14px;border-right:1px solid #ccc}
tr.alt td{background:var(--row-alt)}
tr.active td{background:var(--yellow)}
.num{text-align:center;padding-left:0}
.round-btn{position:absolute;top:2px;width:14px;height:14px;border-radius:50%;color:#fff;font-size:13px;line-height:14px;text-align:center;font-weight:700}
</style>
</head>
<body>
<main class="app">
  <nav class="nav">
    <span class="nav-item" style="left:72px">New Tab</span><span class="nav-sep" style="left:118px"></span>
    <span class="nav-item" style="left:172px">Current Tab</span><span class="nav-sep" style="left:226px"></span>
    <span class="nav-item" style="left:278px">Saved Tab</span><span class="nav-sep" style="left:330px"></span>
    <span class="nav-item" style="left:365px">Tools</span><span class="nav-sep" style="left:402px"></span>
    <span class="nav-item" style="left:445px">Load models</span><span class="nav-sep" style="left:519px"></span>
    <span class="nav-item" style="left:556px">About</span><span class="nav-sep" style="left:594px"></span>
    <span class="nav-item" style="left:668px"><span class="hint-mark">?</span> Hints</span>
    <span class="nav-item" style="left:761px">Colour</span>
    <span class="swatch" style="left:790px;border:3px solid var(--blue);background:#222"></span>
    <span class="swatch" style="left:820px;background:#bbb"></span>
    <span class="swatch" style="left:850px;background:#fff"></span>
  </nav>

  <div class="abs portfolio-select">KAM AA<span class="caret"></span></div>
  <div class="abs doc-button">
    <svg width="38" height="28" viewBox="0 0 38 28"><path d="M13 6h9l4 4v12H13z" fill="none" stroke="#333" stroke-width="1.4"/><path d="M22 6v4h4M16 13h7M16 16h7M16 19h7" stroke="#333" stroke-width="1.2" fill="none"/></svg>
  </div>
  <div class="abs app-title">Vantix 220</div>

  <aside>
    <div class="control-label" style="top:83px">Portfolio Date</div>
    <div class="control select" style="top:98px">6/18/2013</div>
    <div class="control-label" style="top:142px">Currency</div>
    <div class="control select" style="top:156px">USD</div>
    <div class="control-label" style="top:200px">Model Date 06/12/2013</div>
    <div class="control" style="top:214px">Read Model</div>
    <div class="control-label" style="top:258px">Weight Type</div>
    <div class="control select" style="top:272px">Active</div>
    <div class="control-label" style="top:316px">Model</div>
    <div class="control select" style="top:330px">Quantora</div>
    <div class="control-label" style="top:374px">Loss Threshold</div>
    <div class="control" style="top:388px">-10</div>
    <div class="control-label" style="top:430px">Online Key Scenarios</div>
    <div class="check"><svg width="11" height="11" viewBox="0 0 11 11"><path d="M2 6l2.5 2.5L9 2" stroke="#1a6fb0" stroke-width="1.6" fill="none"/></svg></div>
    <div class="control-label" style="top:466px">Current Scenario</div>
    <div class="search"><svg class="abs" style="left:108px;top:7px" width="14" height="14" viewBox="0 0 14 14"><circle cx="5.5" cy="5.5" r="4" stroke="#555" stroke-width="1.5" fill="none"/><path d="M8.5 8.5L13 13" stroke="#555" stroke-width="2"/></svg></div>
  </aside>

  <section aria-label="Scenario chart">
    <div class="tick-y" style="top:80px">-12</div><div class="tick-y" style="top:117px">-13</div><div class="tick-y" style="top:153px">-14</div><div class="tick-y" style="top:190px">-15</div><div class="tick-y" style="top:227px">-16</div><div class="tick-y" style="top:263px">-17</div><div class="tick-y" style="top:300px">-18</div><div class="tick-y" style="top:337px">-19</div><div class="tick-y" style="top:373px">-20</div><div class="tick-y" style="top:410px">-21</div><div class="tick-y" style="top:447px">-22</div><div class="tick-y" style="top:483px">-23</div><div class="tick-y" style="top:520px">-24</div>
    <div class="tick-x" style="left:167px">-24</div><div class="tick-x" style="left:202px">-23</div><div class="tick-x" style="left:238px">-22</div><div class="tick-x" style="left:273px">-21</div><div class="tick-x" style="left:309px">-20</div><div class="tick-x" style="left:344px">-19</div><div class="tick-x" style="left:380px">-18</div><div class="tick-x" style="left:415px">-17</div><div class="tick-x" style="left:450px">-16</div><div class="tick-x" style="left:486px">-15</div><div class="tick-x" style="left:521px">-14</div><div class="tick-x" style="left:557px">-13</div><div class="tick-x" style="left:592px">-12</div>
    <div class="abs chart">
      <svg width="423" height="438" viewBox="0 0 423 438">
        <defs>
          <pattern id="grid" width="35.25" height="36.5" patternUnits="userSpaceOnUse">
            <path d="M0 0V36.5M0 0H35.25" stroke="#3c3c3c" stroke-width="1" fill="none"/>
            <path d="M17.6 0V36.5M0 18.25H35.25" stroke="#2c2c2c" stroke-width="1" fill="none"/>
          </pattern>
        </defs>
        <rect width="423" height="438" fill="url(#grid)"/>
        <path d="M0 308H114M114 308V438" stroke="var(--yellow)" stroke-width="1" fill="none"/>
        <circle cx="44" cy="382" r="4.5" fill="var(--blue)"/>
        <circle cx="309" cy="142" r="4.5" fill="var(--blue)"/>
        <circle cx="336" cy="123" r="4.5" fill="var(--blue)"/>
        <circle cx="114" cy="308" r="5" fill="var(--yellow)" stroke="#fff" stroke-width="1"/>
      </svg>
      <span class="axis-tab" style="left:193px;top:1px">Loss</span>
      <span class="axis-tab" style="left:368px;top:210px;transform:rotate(-90deg);transform-origin:100% 0;white-space:nowrap">Correlation Surprise</span>
    </div>
    <div class="abs tooltip">
      <div class="tooltip-title">STAGFLATION SEVERE</div>
      <div class="tooltip-body">Loss: -18.82<br>Plausibility: 0.00<br>Correlation Surprise: -18.82</div>
    </div>
  </section>

  <section class="abs contrib" style="top:84px">
    <div class="contrib-head">ASSET CONTRIBUTION 10 HIGHEST</div>
    <div class="contrib-plot"></div>
    <div class="row pos" style="top:28px"><span class="name">HRX 6.505</span><span class="date">02/12/67</span><span class="bar" style="left:112px;width:123px"></span><span class="pill" style="left:228px">0.083</span></div>
    <div class="row pos" style="top:44px"><span class="name">TVN 6.02</span><span class="date">02/15/67</span><span class="bar" style="left:112px;width:105px"></span><span class="pill" style="left:200px">0.071</span></div>
    <div class="row pos" style="top:60px"><span class="name">FNBR 6.5</span><span class="date">04/15/37</span><span class="bar" style="left:112px;width:56px"></span><span class="pill" style="left:158px">0.038</span></div>
    <div class="row pos" style="top:76px"><span class="name">GQ 5.5</span><span class="date">12/31/49</span><span class="bar" style="left:112px;width:25px"></span><span class="pill" style="left:126px">0.017</span></div>
    <div class="row pos" style="top:92px"><span class="name">TDLRN 7.875</span><span class="date">01/15/19</span><span class="bar" style="left:112px;width:24px"></span><span class="pill" style="left:124px">0.016</span></div>
    <div class="row pos" style="top:108px"><span class="name">ULX Float</span><span class="date">07/02/14</span><span class="bar" style="left:112px;width:13px"></span><span class="pill" style="left:112px">0.009</span></div>
    <div class="row pos" style="top:124px"><span class="name">WRM 7.506</span><span class="date">05/29/49</span><span class="bar" style="left:112px;width:13px"></span><span class="pill" style="left:112px">0.009</span></div>
    <div class="row pos" style="top:140px"><span class="name">MERIDA 12.5</span><span class="date">02/15/18</span><span class="bar" style="left:112px;width:3px"></span><span class="pill" style="left:112px">0.002</span></div>
    <div class="row pos" style="top:156px"><span class="name">BIOX 10.25</span><span class="date">10/01/15</span><span class="bar" style="left:112px;width:3px"></span><span class="pill" style="left:112px">0.002</span></div>
    <div class="row pos" style="top:172px"><span class="name">YVC 10.25</span><span class="date">02/15/16</span><span class="bar" style="left:112px;width:2px"></span><span class="pill" style="left:112px">0.001</span></div>
    <span class="scale" style="left:112px;top:198px">0.00</span><span class="scale" style="left:142px;top:198px">0.02</span><span class="scale" style="left:172px;top:198px">0.04</span><span class="scale" style="left:202px;top:198px">0.06</span><span class="scale" style="left:232px;top:198px">0.08</span><span class="scale" style="left:260px;top:198px">0.10</span>
  </section>

  <section class="abs contrib" style="top:308px">
    <div class="contrib-head">ASSET CONTRIBUTION 10 LOWEST</div>
    <div class="contrib-plot"></div>
    <div class="row neg" style="top:30px"><span class="name">WQ 7.375</span><span class="date">03/15/32</span><span class="bar" style="left:112px;width:19px"></span><span class="pill" style="left:112px">-0.320</span></div>
    <div class="row neg" style="top:46px"><span class="name">TURKEY 7</span><span class="date">06/05/20</span><span class="bar" style="left:112px;width:19px"></span><span class="pill" style="left:112px">-0.322</span></div>
    <div class="row neg" style="top:62px"><span class="name">TII 0.125</span><span class="date">01/15/22</span><span class="bar" style="left:112px;width:20px"></span><span class="pill" style="left:112px">-0.343</span></div>
    <div class="row neg" style="top:78px"><span class="name">T 3.125</span><span class="date">02/15/43</span><span class="bar" style="left:112px;width:21px"></span><span class="pill" style="left:112px">-0.352</span></div>
    <div class="row neg" style="top:94px"><span class="name">INDON 5.875</span><span class="date">03/13/20</span><span class="bar" style="left:112px;width:21px"></span><span class="pill" style="left:112px">-0.354</span></div>
    <div class="row neg" style="top:110px"><span class="name">WAVU 2005-AR6 X</span><span class="date">02/25/46</span><span class="bar" style="left:112px;width:21px"></span><span class="pill" style="left:112px">-0.360</span></div>
    <div class="row neg" style="top:126px"><span class="name">RUSSIA 4.5</span><span class="date">04/04/22</span><span class="bar" style="left:112px;width:22px"></span><span class="pill" style="left:112px">-0.370</span></div>
    <div class="row neg" style="top:142px"><span class="name">TII 3/875</span><span class="date">04/04/22</span><span class="bar" style="left:112px;width:34px"></span><span class="pill" style="left:120px">-0.577</span></div>
    <div class="row neg" style="top:158px"><span class="name">TII 3.875</span><span class="date">04/15/29</span><span class="bar" style="left:112px;width:53px"></span><span class="pill" style="left:140px">-0.900</span></div>
    <div class="row neg" style="top:174px"><span class="name">AXORA 8.6</span><span class="date">12/15/30</span><span class="bar" style="left:112px;width:117px"></span><span class="pill" style="left:200px">-1.975</span></div>
    <span class="scale" style="left:112px;top:198px">0.0</span><span class="scale" style="left:142px;top:198px">-0.5</span><span class="scale" style="left:172px;top:198px">-1.0</span><span class="scale" style="left:202px;top:198px">-1.5</span><span class="scale" style="left:232px;top:198px">-2.0</span><span class="scale" style="left:260px;top:198px">-2.5</span>
  </section>

  <section class="abs table-panel" style="left:12px;width:420px">
    <div class="table-title">SHOCKS</div>
    <table>
      <tr><th style="width:214px">Name</th><th style="width:126px">Type</th><th>Shock</th></tr>
      <tr><td>United States</td><td>Equity Indexx</td><td class="num">-15</td></tr>
      <tr class="alt"><td>Gold</td><td>Macro/Styxxx</td><td class="num">60</td></tr>
      <tr><td>3 Years US Government</td><td>Interest Ratxx</td><td class="num">3</td></tr>
      <tr class="alt"><td>30 Years US Government</td><td>Interest Ratxx</td><td class="num">3</td></tr>
    </table>
  </section>

  <section class="abs table-panel" style="left:443px;width:425px">
    <div class="table-title">CURRENT SCENARIO</div>
    <span class="round-btn" style="left:344px;background:var(--green)">+</span>
    <span class="round-btn" style="left:382px;background:var(--red)">−</span>
    <table>
      <tr><th style="width:150px">Name</th><th style="width:74px">Loss</th><th style="width:90px">Correlation</th><th>Planxxxx</th></tr>
      <tr><td>US Treasury Interest</td><td>-21.57</td><td>-21.57</td><td></td></tr>
      <tr class="active"><td>Stagflation Severe</td><td>-18.82</td><td>-18.82</td><td></td></tr>
      <tr><td>Stagflation</td><td>-11.1</td><td>-11.1</td><td></td></tr>
      <tr class="alt"><td>US Treasury Interest</td><td>-10.87</td><td>-10.87</td><td></td></tr>
    </table>
  </section>
</main>
</body>
</html>
```